Web Design Project

My website was fine - years ago. But it's way, way overdue for an overhaul. When I started my business almost 20 years ago, I wanted to be edgy. And my website was just that. Color, style, voice. Edgy. Today, my clients are corporations. I'm older, more experienced - but still a little edgy. It's controlled edge. What I want now is sophisticated. Savvy. Corporate but cool. Grown up.

My clients are primarily - but not exclusively - in healthcare. But I don't want a healthcare site. I provide the following services:
1. Writing - white papers, brochures, web pages, speechwriting, etc.
2. Marketing strategy
3. Public relations services
4. Thought leader development
5. Training
I couldn't upload all the icons but I can send them. They correspond with the pages as follows and should be used in the design:

1. Writing- nib.png
2. Marketing strategy-compass.png
3. Public relations services-microphone.png
4. Thought leader development-lightbulb.png
5. Training: cogs-training.png or key.png

I will have a blog, and a portfolio of some kind.

I don't want something that looks like a template.
Updates

Reason: Just made this a committed payment. I apologize for not doing so from the start. Nobody should work for free.

Reason: Several folks have asked to resubmit, and it has taken me a while to provide feedback.

Dear Designers,

I am so sorry to have been so slow to select. I've had professional and personal issues to deal with. I am actively trying to select a design, however, and will do so in the next two days. Thanks so much for your patience and hard work.

Rhoda

Thanks so much to everyone who has submitted a design. I had great luck crowdsourcing my logo, but I'm starting to realize that website design is a totally different animal. All of your designs are great, but they all look exactly like templates. And maybe that's the way it's supposed to be, the way it should be. I don't want to use stock photography. It needs to be more personalized than that. I'm open to illustration or even using my own photo on the site, but stock photography won't work for me. If anyone wants to submit something else - and I understand if you don't - please feel free. 

Target Market(s)

C-suite executives; corporations, larger businesses who need marketing writing

Industry/Entity Type

Healthcare

Requirements
Must have
• Logo (somewhere)
Icons
Nice to have
• Level-specific page design (e.g, Home = Level 1, Tabs = Level 2, etc). I'd like it to have a certain order.

```html
<!DOCTYPE html>
<html lang="en">
<head>
<meta charset="utf-8">
<title>Keystone Writing</title>
<link rel="stylesheet" href="https://fonts.googleapis.com/css2?family=Open+Sans:wght@400;600;700&family=Lora:ital,wght@0,400;0,700;1,400&display=swap">
<style>
:root{
  --purple:#5a2a82;
  --orange:#f39a1e;
  --ink:#333;
  --muted:#777;
  --page:#ececec;
  --panel:#fff;
  --dark:#262626;
  --icon:#4a4a4a;
}
*{box-sizing:border-box;margin:0;padding:0}
html,body{width:732px;height:1200px;overflow:hidden}
body{background:var(--page);font-family:"Open Sans",Arial,sans-serif;color:var(--ink);font-size:7px;line-height:1.4}
.wrap{width:650px;margin:0 auto;position:relative}

.site-header{height:78px;background:var(--panel)}
.site-header .wrap{height:78px}
.brand{position:absolute;left:0;top:16px;display:flex;align-items:center;gap:6px;font-family:"Open Sans",Arial,sans-serif;font-weight:600;font-size:17px;color:var(--ink)}
.brand-dot{width:12px;height:12px;background:var(--orange)}
.main-nav{position:absolute;right:0;top:14px;display:flex;gap:2px}
.main-nav a{font-size:7px;font-weight:600;color:#555;text-decoration:none;padding:6px 7px;border-bottom:3px solid transparent}
.main-nav a.active{color:var(--purple);border-bottom-color:var(--orange)}
.social{position:absolute;right:0;top:52px;display:flex;gap:4px}
.social span{width:11px;height:11px;background:#8a8a8a;border-radius:2px}

.hero{height:277px;background:var(--panel);padding:0 0 8px}
.hero-photo{position:relative;height:269px;width:660px;margin:0 auto;background:linear-gradient(135deg,#dfe4ea 0%,#9aa4b0 40%,#3c4450 75%,#20252d 100%)}
.hero-caption{position:absolute;left:0;right:0;bottom:0;height:40px;background:rgba(20,20,20,.55);color:#fff;text-align:center;font-weight:700;font-size:8px;padding-top:9px;letter-spacing:.5px}

.ask-bar{height:37px;background:var(--panel);border-top:1px solid #ddd}
.ask-bar .wrap{height:37px;display:flex;align-items:center;justify-content:space-between}
.ask-bar h3{color:var(--orange);font-size:9px;font-weight:700}
.btn{display:inline-block;background:var(--orange);color:#fff;font-size:6.5px;font-weight:700;padding:4px 12px;text-decoration:none}

.services{height:198px;background:var(--panel)}
.services .wrap{display:flex;justify-content:space-between;padding-top:14px}
.service{width:120px;text-align:center}
.service svg{width:52px;height:52px;display:block;margin:0 auto 6px}
.service h4{font-size:8.5px;font-weight:700;color:#444;margin-bottom:8px}
.service p{text-align:left;color:var(--muted);font-size:6.5px;margin-bottom:10px;min-height:44px}
.more-link{display:block;text-align:left;font-size:6.5px;color:#555;font-weight:600}
.service:first-child .more-link{color:var(--orange)}

.statement{height:55px;text-align:center;padding-top:12px}
.statement q{font-family:"Lora",Georgia,serif;font-style:italic;font-size:13px;color:#444;quotes:"« " " »"}
.statement cite{display:block;font-style:normal;font-size:7px;color:var(--muted);margin-top:2px;padding-left:160px}

.intro{height:175px}
.intro .wrap{display:flex;gap:16px;background:var(--panel);padding:10px;height:168px}
.intro h2{font-size:10px;font-weight:700;color:#333;margin-bottom:8px;border-bottom:1px solid #ddd;padding-bottom:4px}
.col{flex:1}
.hello-photo{height:54px;background:linear-gradient(90deg,#c9d3df,#8f9cab);margin-bottom:6px}
.hello-lead{color:var(--orange);font-size:10px;line-height:1.25;margin-bottom:5px}
.col p{color:var(--muted);font-size:6.5px}
.offer-list{list-style:none}
.offer-list li{font-size:6.5px;color:#555;padding:3px 0 3px 10px;border-bottom:1px dotted #ccc;position:relative}
.offer-list li::before{content:"";position:absolute;left:0;top:6px;width:4px;height:4px;background:var(--purple);border-radius:50%}
.testimonial{font-family:"Lora",Georgia,serif;font-style:italic;color:var(--orange);font-size:8px;line-height:1.45}
.reviewer{text-align:right;font-size:6.5px;color:#555;margin-top:8px}

.notes{height:145px}
.notes .wrap{display:flex;gap:10px}
.note{flex:1;background:var(--panel);border:1px solid #d8d8d8;height:135px;padding:8px}
.note h3{font-size:8.5px;font-weight:700;color:#333;border-bottom:1px solid #ddd;padding-bottom:4px;margin-bottom:6px}
.note p{color:var(--muted);font-size:6.5px;height:62px}
.note .btn{padding:4px 10px}

.partners{height:57px}
.partners h3{font-size:9px;font-weight:700;color:#444;margin-bottom:6px}
.partner-row{display:flex;justify-content:space-between;align-items:center}
.partner-row span{width:62px;height:20px;background:#c4c4c4;border-radius:2px}

.site-footer{height:178px;background:var(--dark);color:#ccc;padding-top:14px}
.site-footer .wrap{display:flex;gap:22px}
.site-footer h4{font-family:"Lora",Georgia,serif;font-size:10px;color:#fff;margin-bottom:8px;font-weight:400}
.links{list-style:none}
.links li{font-size:6.5px;padding:2px 0 2px 8px;position:relative}
.links li::before{content:"›";position:absolute;left:0;color:var(--orange)}
.contact p{font-size:6.5px;margin-bottom:6px;display:flex;gap:5px;align-items:center}
.contact svg{width:8px;height:8px;flex:none}
.footer-brand{margin-left:auto;text-align:right}
.footer-name{font-family:"Open Sans",Arial,sans-serif;font-size:15px;color:#999;font-weight:600;display:block;margin-top:12px}
.copyright{font-size:6px;color:#888;margin-top:40px}
</style>
</head>
<body>

<header class="site-header">
  <div class="wrap">
    <div class="brand"><span class="brand-dot"></span>Keystone Writing</div>
    <nav class="main-nav">
      <a href="#">HOME</a><a href="#" class="active">ABOUT US</a><a href="#">SERVICES</a><a href="#">PORTFOLIO</a><a href="#">OUR BLOG</a><a href="#">ABOUT KEYSTONE</a><a href="#">CONTACT US</a>
    </nav>
    <div class="social"><span></span><span></span><span></span><span></span></div>
  </div>
</header>

<section class="hero">
  <div class="hero-photo" role="img" aria-label="Photo of business people meeting around a desk">
    <div class="hero-caption">INSURING YOUR FUTURE ... TODAY<br>HELPING YOUR PLAN FOR TOMORROW ... TODAY</div>
  </div>
</section>

<section class="ask-bar">
  <div class="wrap"><h3>ASK PROFESSIONALS</h3><a class="btn" href="#">CLICK HERE</a></div>
</section>

<section class="services">
  <div class="wrap">
    <div class="service">
      <svg viewBox="0 0 52 52"><circle cx="26" cy="26" r="25" fill="var(--icon)"/><circle cx="26" cy="26" r="13" fill="none" stroke="#fff" stroke-width="2"/><path d="M26 15 L29 26 L26 37 L23 26Z" fill="#fff"/></svg>
      <h4>MARKETING STRATEGY</h4>
      <p>Focused plans that tie each campaign to clear business goals and results.</p>
      <a class="more-link">Read More ›</a>
    </div>
    <div class="service">
      <svg viewBox="0 0 52 52"><circle cx="26" cy="26" r="25" fill="var(--icon)"/><circle cx="22" cy="28" r="8" fill="none" stroke="#fff" stroke-width="4" stroke-dasharray="3 2"/><circle cx="33" cy="19" r="5" fill="none" stroke="#fff" stroke-width="3" stroke-dasharray="2 2"/></svg>
      <h4>TRAINING</h4>
      <p>Hands-on sessions that help your team write and present with confidence.</p>
      <a class="more-link">Read More ›</a>
    </div>
    <div class="service">
      <svg viewBox="0 0 52 52"><circle cx="26" cy="26" r="25" fill="var(--icon)"/><rect x="21" y="13" width="10" height="17" rx="5" fill="#fff"/><path d="M17 26 a9 9 0 0 0 18 0 M26 35 V40 M21 40 H31" fill="none" stroke="#fff" stroke-width="2"/></svg>
      <h4>PUBLIC RELATIONS</h4>
      <p>Media outreach and stories that put your company in the right light.</p>
      <a class="more-link">Read More ›</a>
    </div>
    <div class="service">
      <svg viewBox="0 0 52 52"><circle cx="26" cy="26" r="25" fill="var(--icon)"/><circle cx="26" cy="23" r="9" fill="#fff"/><rect x="22" y="31" width="8" height="7" fill="#fff"/></svg>
      <h4>THOUGHT LEADER</h4>
      <p>Positioning your leaders as trusted voices in their field and market.</p>
      <a class="more-link">Read More ›</a>
    </div>
    <div class="service">
      <svg viewBox="0 0 52 52"><circle cx="26" cy="26" r="25" fill="var(--icon)"/><path d="M26 12 L35 26 L26 40 L17 26Z" fill="#fff"/><circle cx="26" cy="27" r="2" fill="var(--icon)"/><path d="M26 29 V38" stroke="var(--icon)" stroke-width="1.2"/></svg>
      <h4>WRITING</h4>
      <p>White papers, brochures, web pages and speeches written to persuade readers.</p>
      <a class="more-link">Read More ›</a>
    </div>
  </div>
</section>

<section class="statement">
  <q>Our work is dedicated to the prosperity of our clients! Think of your Profit</q>
  <cite>Dana Whitfield</cite>
</section>

<section class="intro">
  <div class="wrap">
    <div class="col">
      <h2>HELLO THERE!</h2>
      <div class="hello-photo" role="img" aria-label="Photo of a smiling business team"></div>
      <div class="hello-lead">Lorem Ipsum is simply dummy text of the printing and typesetting industry.</div>
      <p>A short welcome from our founder about the way we work with clients, what we value and how we help leaders share ideas that matter.</p>
    </div>
    <div class="col">
      <h2>WHAT WE OFFER</h2>
      <ul class="offer-list">
        <li>Corporate writing</li><li>Brand strategy</li><li>Media relations</li><li>Speechwriting</li><li>Leadership programs</li><li>Web content</li>
      </ul>
    </div>
    <div class="col">
      <h2>TESTIMONIALS</h2>
      <p class="testimonial">"They took the time to learn our business and turned a complex story into clear, sharp copy. Our board, our clients and our staff all noticed the difference within weeks. We will keep working with them."</p>
      <div class="reviewer">Mr. Paul Everly<br>Manager</div>
    </div>
  </div>
</section>

<section class="notes">
  <div class="wrap">
    <article class="note"><h3>WHAT WE DO!</h3><p>We write, plan and shape messages for healthcare firms and other corporate clients who need clear words that move readers to act.</p><a class="btn" href="#">MORE</a></article>
    <article class="note"><h3>WHAT'S UP?</h3><p>News from the studio: a new white paper series, a fresh training program and notes from recent events with our clients.</p><a class="btn" href="#">MORE</a></article>
    <article class="note"><h3>DID YOU KNOW?</h3><p>Most executives read only the first two lines of a report. We make sure those lines carry the message you need them to hear.</p><a class="btn" href="#">MORE</a></article>
  </div>
</section>

<section class="partners">
  <div class="wrap">
    <h3>FOLKS WHO DIG US</h3>
    <div class="partner-row"><span></span><span></span><span></span><span></span><span></span><span></span><span></span><span></span></div>
  </div>
</section>

<footer class="site-footer">
  <div class="wrap">
    <div>
      <h4>Quick Links</h4>
      <ul class="links"><li>Home</li><li>About Us</li><li>Services</li><li>Portfolio</li><li>Our Blog</li></ul>
    </div>
    <div>
      <h4>&nbsp;</h4>
      <ul class="links"><li>About Keystone</li><li>Why Keystone?</li><li>Our Purpose</li><li>Contact Us</li></ul>
    </div>
    <div class="contact">
      <h4>Contact Details</h4>
      <p><svg viewBox="0 0 10 10"><path d="M5 0a3.5 3.5 0 0 0-3.5 3.5C1.5 6 5 10 5 10s3.5-4 3.5-6.5A3.5 3.5 0 0 0 5 0z" fill="var(--orange)"/></svg>Suite 200, 48 Harbor Lane, Westfield, NY 10001</p>
      <p><svg viewBox="0 0 10 10"><path d="M2 0h2l1 3-1.5 1a6 6 0 0 0 2.5 2.5L7 5l3 1v2c0 1-1 2-2 2A8 8 0 0 1 0 2c0-1 1-2 2-2z" fill="var(--orange)"/></svg>(555) 017-4388</p>
      <p><svg viewBox="0 0 10 10"><rect y="2" width="10" height="6" fill="var(--orange)"/><path d="M0 2l5 3.5L10 2" stroke="var(--dark)" fill="none"/></svg>hello@keystonewriting.com</p>
    </div>
    <div class="footer-brand">
      <span class="footer-name">Keystone Writing</span>
      <div class="copyright">© Copyright 2014 Keystone Writing. All Rights Reserved.</div>
    </div>
  </div>
</footer>

</body>
</html>
```